TrueGrindz Complete Stationery - Logo already designed

I already have the logo designed see attached. I need have a full set of stationary and business card designed for printing. I have attached an example of what I mean.

Please feel free to be creative. Also you can use the X in the logo by its self if you think it will work.

My details:

Name: Corwin Lestak
Social media handles: @corwinlestak
W: corwinlestak.com
E: info@corwinlestak.com
​P: 08 7493 5286
PO Box 7382, Marrowdale 6087
ABN 83 402 719 265

Target Market(s)

Anyone looking to be inspired.

Industry/Entity Type

Business

Font styles to use
Sans Serif

Colors
fbee3e
000000

Requirements
Must have
• My details:
• Name: Corwin Lestak
• Social media handles: @corwinlestak
• W: corwinlestak.com
• E: info@corwinlestak.com
• ​P: 08 7493 5286
• PO Box 7382, Marrowdale 6087
• ABN 83 402 719 265
Nice to have
• Something a little different
Should not have
• must not look tacky.

```html
<!DOCTYPE html>
<html lang="en">
<head>
<meta charset="utf-8">
<title>TrueGrindz Stationery</title>
<link href="https://fonts.googleapis.com/css2?family=Open+Sans:ital,wght@0,400;0,600;0,800;1,700&display=swap" rel="stylesheet">
<style>
:root{
  --yellow:#f9c91c;
  --yellow-soft:#fbe27a;
  --ink:#232323;
  --charcoal:#3b3b3b;
  --paper:#ffffff;
  --paper-warm:#fdfbf3;
  --backdrop:#e4e4e4;
}
*{margin:0;padding:0;box-sizing:border-box}
html,body{width:745px;height:1200px;overflow:hidden}
body{background:var(--backdrop);font-family:"Open Sans",Arial,sans-serif;color:var(--ink);position:relative}
.sheet{position:absolute;overflow:hidden;box-shadow:0 2px 6px rgba(0,0,0,.18)}
.wordmark{font-family:"Open Sans",Arial,sans-serif;font-weight:800;text-transform:uppercase;color:var(--ink);letter-spacing:-.02em;white-space:nowrap;line-height:1}
.foot{position:absolute;left:0;right:0;bottom:0;background:var(--charcoal)}
.foot .tab{position:absolute;right:0;bottom:0;height:100%;background:var(--yellow);clip-path:polygon(12% 0,100% 0,100% 100%,0 100%);display:flex;align-items:center;justify-content:flex-end;font-weight:600;color:var(--ink);white-space:nowrap}
.details{list-style:none;line-height:1.45}
.details li{display:flex;align-items:center;white-space:nowrap}
.details svg{flex:none;fill:var(--yellow)}

/* folder */
.folder{left:70px;top:70px;width:250px;height:350px;background:linear-gradient(160deg,var(--yellow-soft) 0%,var(--yellow) 55%,#f6c010 100%)}
.folder .wordmark{position:absolute;left:0;right:0;top:160px;text-align:center;font-size:33px}

/* letterhead */
.letterhead{left:345px;top:75px;width:250px;height:345px;background:linear-gradient(160deg,var(--paper) 0%,var(--paper-warm) 100%)}
.letterhead .wordmark{position:absolute;left:16px;top:26px;font-size:13px}
.letterhead .contact{position:absolute;left:150px;top:12px;padding-left:6px;border-left:1px solid var(--ink);font-size:4.6px}
.letterhead .contact strong{display:block;font-size:5.4px;font-weight:600}
.letterhead .foot{height:9px}
.letterhead .tab{width:72px;font-size:6px;padding-right:6px}

/* compliment slip */
.slip{left:40px;top:445px;width:245px;height:125px;background:linear-gradient(160deg,var(--paper),var(--paper-warm))}
.slip .wordmark{position:absolute;left:10px;top:15px;font-size:12px}
.slip .contact{position:absolute;left:8px;top:77px;font-size:4.3px}
.slip .contact strong{display:block;font-size:5px;font-weight:600}
.slip .details svg{width:4px;height:4px;margin-right:3px}
.slip .foot{height:8px}
.slip .tab{width:72px;font-size:5.5px;padding-right:8px}

/* envelope */
.envelope{left:310px;top:445px;width:240px;height:125px;background:var(--paper)}
.envelope .flap{position:absolute;left:0;right:0;top:0;height:26px;background:linear-gradient(160deg,var(--yellow-soft),var(--yellow))}
.envelope .flap .wordmark{position:absolute;left:0;right:0;top:8px;text-align:center;font-size:11px}
.envelope .return{position:absolute;right:12px;bottom:14px;font-size:10px}

/* small cards */
.mini-back{left:595px;top:448px;width:112px;height:56px;background:linear-gradient(160deg,var(--yellow-soft),var(--yellow))}
.mini-back .wordmark{position:absolute;left:0;right:0;top:21px;text-align:center;font-size:13px}
.mini-front{left:595px;top:512px;width:112px;height:56px;background:var(--paper)}
.mini-front .name{position:absolute;left:6px;top:6px;font-size:4.8px;font-weight:700;font-style:italic}
.mini-front .contact{position:absolute;left:6px;top:15px;font-size:3.4px}
.mini-front .details svg{width:3px;height:3px;margin-right:2px}
.mini-front .foot{height:5px}
.mini-front .tab{width:30px;font-size:3.4px;padding-right:3px}

/* large business card front */
.card-front{left:60px;top:690px;width:390px;height:223px;background:linear-gradient(160deg,#ffffff 0%,#f3f3f3 100%)}
.card-front .name{position:absolute;left:26px;top:34px;font-size:19px;font-weight:700;font-style:italic}
.card-front .rule{position:absolute;left:0;top:66px;width:225px;height:3px;background:var(--yellow)}
.card-front .contact{position:absolute;left:28px;top:104px;font-size:11px;line-height:1.36}
.card-front .details svg{width:9px;height:9px;margin-right:8px}
.card-front .details li.no-icon{padding-left:17px}
.card-front .wordmark{position:absolute;right:18px;top:124px;font-size:19px}
.card-front .foot{height:20px;background:linear-gradient(90deg,#2b2b2b,#5a5a5a 60%,#2b2b2b)}
.card-front .tab{width:150px;font-size:12px;padding-right:16px}

/* large business card back */
.card-back{left:295px;top:935px;width:390px;height:223px;background:linear-gradient(150deg,var(--yellow-soft) 0%,var(--yellow) 55%,#f3bd0f 100%)}
.card-back .wordmark{position:absolute;left:0;right:0;top:88px;text-align:center;font-size:46px}
</style>
</head>
<body>

<svg width="0" height="0" style="position:absolute" aria-hidden="true">
  <symbol id="icon-pin" viewBox="0 0 10 10"><path d="M5 0a3.5 3.5 0 0 0-3.5 3.5C1.5 6 5 10 5 10s3.5-4 3.5-6.5A3.5 3.5 0 0 0 5 0zm0 5a1.5 1.5 0 1 1 0-3 1.5 1.5 0 0 1 0 3z"/></symbol>
  <symbol id="icon-phone" viewBox="0 0 10 10"><path d="M2 0l2 2.5-1.2 1.2a6 6 0 0 0 3.5 3.5L7.5 6 10 8l-1.2 1.6C4.5 10 0 5.5.4 1.2z"/></symbol>
  <symbol id="icon-mail" viewBox="0 0 10 10"><path d="M0 2h10v6H0zM.8 2.6 5 5.6l4.2-3" stroke="#fff" stroke-width=".7"/></symbol>
  <symbol id="icon-web" viewBox="0 0 10 10"><circle cx="5" cy="5" r="5"/><path d="M0 5h10M5 0c-2.5 3-2.5 7 0 10M5 0c2.5 3 2.5 7 0 10" stroke="#fff" stroke-width=".6" fill="none"/></symbol>
</svg>

<section class="sheet folder" aria-label="Presentation folder">
  <div class="wordmark">TrueGrindz</div>
</section>

<section class="sheet letterhead" aria-label="Letterhead">
  <div class="wordmark">TrueGrindz</div>
  <div class="contact">
    <strong>Corwin Lestak</strong>
    PO Box 7382, Marrowdale 6087<br>
    08 7493 5286<br>
    info@corwinlestak.com<br>
    corwinlestak.com<br>
    ABN 83 402 719 265
  </div>
  <div class="foot"><div class="tab">@corwinlestak</div></div>
</section>

<section class="sheet slip" aria-label="Compliment slip">
  <div class="wordmark">TrueGrindz</div>
  <div class="contact">
    <strong>Corwin Lestak</strong>
    <ul class="details">
      <li><svg><use href="#icon-pin"/></svg>PO Box 7382, Marrowdale 6087</li>
      <li><svg><use href="#icon-phone"/></svg>08 7493 5286</li>
      <li><svg><use href="#icon-mail"/></svg>info@corwinlestak.com</li>
      <li><svg><use href="#icon-web"/></svg>corwinlestak.com</li>
      <li>ABN 83 402 719 265</li>
    </ul>
  </div>
  <div class="foot"><div class="tab">@corwinlestak</div></div>
</section>

<section class="sheet envelope" aria-label="DL envelope">
  <div class="flap"><div class="wordmark">TrueGrindz</div></div>
  <div class="wordmark return">TrueGrindz</div>
</section>

<section class="sheet mini-back" aria-label="Business card back">
  <div class="wordmark">TrueGrindz</div>
</section>

<section class="sheet mini-front" aria-label="Business card front">
  <div class="name">Corwin Lestak</div>
  <div class="contact">
    <ul class="details">
      <li><svg><use href="#icon-pin"/></svg>PO Box 7382, Marrowdale 6087</li>
      <li><svg><use href="#icon-phone"/></svg>08 7493 5286</li>
      <li><svg><use href="#icon-mail"/></svg>info@corwinlestak.com</li>
      <li><svg><use href="#icon-web"/></svg>corwinlestak.com</li>
      <li>ABN 83 402 719 265</li>
    </ul>
  </div>
  <div class="foot"><div class="tab">@corwinlestak</div></div>
</section>

<section class="sheet card-front" aria-label="Business card front, large">
  <div class="name">Corwin Lestak</div>
  <div class="rule"></div>
  <div class="contact">
    <ul class="details">
      <li><svg><use href="#icon-pin"/></svg>PO Box 7382, Marrowdale 6087</li>
      <li><svg><use href="#icon-phone"/></svg>08 7493 5286</li>
      <li><svg><use href="#icon-mail"/></svg>info@corwinlestak.com</li>
      <li><svg><use href="#icon-web"/></svg>corwinlestak.com</li>
      <li class="no-icon">ABN 83 402 719 265</li>
    </ul>
  </div>
  <div class="wordmark">TrueGrindz</div>
  <div class="foot"><div class="tab">@corwinlestak</div></div>
</section>

<section class="sheet card-back" aria-label="Business card back, large">
  <div class="wordmark">TrueGrindz</div>
</section>

</body>
</html>
```